Mattress sale flyer front and back

FLYER SIZE!! front and back!
4.25" X 5.5"
or
10.7cm X 13.9 cm

This flyer needs to show the prices
twin.....$99
full.......$159
queen...$199
king....$299

the phone number........(786)555-0147
the address ..........10420 sw 172st miami fl 33157
if possible a map would be appreciated

possible brands to include.......Dormo, Kellbrook, vale & pruitt, lunadown

ATTACHED IS OUR OLD FLYER WITH OUTDATED INFORMATION, I WOULD LIKE SOMETHING SIMILAR. JUST ADD A LITTLE PRICE LIST AND A MAP

***FRONT AND BACK PLEASE****

```html
<!DOCTYPE html>
<html lang="en">
<head>
<meta charset="utf-8">
<title>Bayside Mattress Outlet – Sale Flyer Front and Back</title>
<link href="https://fonts.googleapis.com/css2?family=Roboto+Condensed:wght@400;700&family=Roboto:wght@400;700&display=swap" rel="stylesheet">
<style>
  :root{
    --page:#f0f0f0;
    --white:#ffffff;
    --sky:#1ab6d3;
    --sky-deep:#0e8fb0;
    --sky-light:#7fd8ea;
    --sky-pale:#c9eef6;
    --ink:#333a3f;
    --grey:#6b6f73;
    --shadow:#4a4f54;
    --navy:#1e3569;
  }
  *{box-sizing:border-box;margin:0;padding:0}
  html,body{width:1200px;height:760px;overflow:hidden;background:var(--page)}
  body{position:relative;font-family:"Roboto",Arial,sans-serif}

  .flyer{position:absolute;top:18px;width:552px;height:716px;background:var(--white);overflow:hidden;box-shadow:0 1px 6px rgba(0,0,0,.18)}
  .flyer--front{left:36px}
  .flyer--back{left:618px}
  .flyer__bg{position:absolute;inset:0;width:100%;height:100%}

  .headline{position:absolute;left:0;width:100%;text-align:center;font-family:"Roboto Condensed",Arial,sans-serif;font-weight:700;color:var(--white)}
  .headline__title{top:44px;font-size:45px;letter-spacing:.5px;text-shadow:0 2px 3px rgba(0,60,90,.35)}
  .headline__sub{top:100px;font-size:15px;letter-spacing:3.2px}

  .photo{position:absolute}
  .photo--mattress-hero{left:54px;top:140px;width:450px;height:170px;border-radius:10px;background:linear-gradient(180deg,#fbfbfb 0%,#e3e6e8 60%,#9aa0a5 78%,#e9ecee 100%)}
  .photo--family{left:26px;top:330px;width:170px;height:266px;border-radius:60px 60px 8px 8px;background:linear-gradient(180deg,#d9c2ae 0%,#a9c3da 40%,#6d86a4 100%)}
  .photo--bed{left:42px;width:118px;height:80px;border-radius:6px;background:linear-gradient(180deg,#ffffff 0%,#e4e7ea 70%,#8c9297 100%)}
  .photo--woman{left:378px;top:58px;width:150px;height:372px;border-radius:70px 70px 12px 12px;background:linear-gradient(180deg,#b88a6e 0%,#cfd8e2 30%,#a9c7e2 62%,#d8e6f2 100%)}

  .call{position:absolute;border-radius:50%;background:var(--white);border:7px solid var(--sky);box-shadow:10px 8px 0 var(--shadow);text-align:center;color:var(--sky);font-family:"Roboto Condensed",Arial,sans-serif}
  .call__word{display:block;font-weight:700;line-height:1}
  .call__phone{display:block;color:var(--ink);font-weight:700}
  .flyer--front .call{left:296px;top:188px;width:176px;height:176px;padding-top:32px}
  .flyer--front .call__word{font-size:66px}
  .flyer--front .call__phone{font-size:22px;margin-top:2px}
  .flyer--back .call{left:312px;top:384px;width:212px;height:212px;padding-top:42px}
  .flyer--back .call__word{font-size:80px}
  .flyer--back .call__phone{font-size:25px;margin-top:4px}

  .brand{position:absolute;text-align:center;color:var(--ink);font-family:"Roboto Condensed",Arial,sans-serif;font-weight:400}
  .brand__name{display:block;font-size:38px;letter-spacing:.5px;line-height:1}
  .brand__sub{display:block;font-size:17px;letter-spacing:7px;margin-top:4px}
  .flyer--front .brand{left:196px;top:430px;width:320px}
  .flyer--back .brand{left:30px;top:494px;width:290px}
  .flyer--back .brand__name{font-size:33px}

  .address{position:absolute;font-family:"Roboto Condensed",Arial,sans-serif;font-size:20px;color:var(--sky);white-space:nowrap}
  .flyer--front .address{left:206px;top:522px}
  .flyer--back .address{left:48px;top:592px;font-size:18px}

  .offers{position:absolute;left:38px;top:606px;font-family:"Roboto Condensed",Arial,sans-serif;font-weight:700;font-size:23px;color:var(--ink);transform:rotate(-8deg);transform-origin:left center;white-space:nowrap}

  .partners{position:absolute;left:18px;right:14px;top:654px;display:flex;align-items:center;justify-content:space-between;font-family:"Roboto Condensed",Arial,sans-serif}
  .partners__item{font-size:17px;font-weight:700;color:var(--navy);display:flex;align-items:center;gap:5px;white-space:nowrap}
  .partners__dot{width:12px;height:12px;background:var(--sky);display:inline-block}
  .partners__more{font-size:14px;font-weight:700;color:var(--navy);line-height:1.15}

  .price-list{position:absolute;left:0;top:0;width:100%;height:100%}
  .price{position:absolute;left:168px;width:86px;height:86px;border-radius:50%;background:var(--white);border:6px solid var(--sky);box-shadow:6px 4px 0 var(--shadow);display:flex;align-items:center;justify-content:center;font-family:"Roboto Condensed",Arial,sans-serif;font-weight:700;font-size:24px;color:var(--ink)}
  .price-label{position:absolute;left:264px;font-family:"Roboto Condensed",Arial,sans-serif;font-weight:700;font-size:20px;color:var(--white);letter-spacing:.5px}
</style>
</head>
<body>

<section class="flyer flyer--front" aria-label="Flyer front">
  <svg class="flyer__bg" viewBox="0 0 552 716" preserveAspectRatio="none" aria-hidden="true">
    <defs>
      <linearGradient id="front-sky" x1="0" y1="0" x2="0" y2="1">
        <stop offset="0" stop-color="#0e9fc2"/>
        <stop offset=".6" stop-color="#22bdd9"/>
        <stop offset="1" stop-color="#8fdcec"/>
      </linearGradient>
    </defs>
    <path d="M0 0H552V300C430 296 300 330 160 380 100 400 40 410 0 412Z" fill="url(#front-sky)"/>
    <path d="M552 220C440 250 330 290 200 330 130 350 60 360 0 362V412C60 404 140 380 220 350 340 310 450 296 552 300Z" fill="#bfe9f3" opacity=".7"/>
    <path d="M552 60C470 120 380 150 250 170 180 180 90 182 0 176V196C110 202 220 196 320 176 430 152 500 110 552 80Z" fill="#ffffff" opacity=".18"/>
    <path d="M0 680C150 650 330 600 552 560V598C360 628 170 672 0 706Z" fill="var(--sky)"/>
    <path d="M0 706C170 672 360 628 552 598V716H0Z" fill="#ffffff"/>
    <path d="M404 556C450 548 490 538 520 524" stroke="var(--shadow)" stroke-width="4" fill="none"/>
    <path d="M380 596C440 588 490 566 520 532" stroke="var(--shadow)" stroke-width="14" fill="none" stroke-linecap="round"/>
    <path d="M506 520L546 512 530 552Z" fill="var(--shadow)"/>
  </svg>

  <h1 class="headline headline__title">EXPERIENCE THE COMFORT</h1>
  <p class="headline headline__sub">FIND THE MATTRESS THAT IS MEANT FOR YOU</p>

  <div class="photo photo--mattress-hero" role="img" aria-label="Photo of a thick white pillow-top mattress"></div>
  <div class="photo photo--family" role="img" aria-label="Photo of a smiling family of four pointing upward"></div>

  <div class="call"><span class="call__word">CALL</span><span class="call__phone">(786)555-0147</span></div>

  <div class="brand"><span class="brand__name">Bayside Mattress</span><span class="brand__sub">OUTLET</span></div>
  <p class="address">10420 SW, 172ST, MIAMI, FL 33157</p>

  <p class="offers">CHECK OUT THE OFFERS TODAY!!!</p>

  <div class="partners">
    <span class="partners__item"><i class="partners__dot"></i>KELLBROOK</span>
    <span class="partners__item">Dormo</span>
    <span class="partners__item">Restova</span>
    <span class="partners__item">Vale &amp; Pruitt</span>
    <span class="partners__more">and other<br>great brand names!</span>
  </div>
</section>

<section class="flyer flyer--back" aria-label="Flyer back">
  <svg class="flyer__bg" viewBox="0 0 552 716" preserveAspectRatio="none" aria-hidden="true">
    <defs>
      <linearGradient id="back-sky" x1="0" y1="0" x2="0" y2="1">
        <stop offset="0" stop-color="#0e9fc2"/>
        <stop offset=".7" stop-color="#22bdd9"/>
        <stop offset="1" stop-color="#8fdcec"/>
      </linearGradient>
    </defs>
    <path d="M0 0H552V440C430 420 300 420 180 430 110 436 50 444 0 452Z" fill="url(#back-sky)"/>
    <path d="M0 28C140 60 300 54 552 6V22C300 74 140 80 0 50Z" fill="#ffffff" opacity=".55"/>
    <path d="M0 146C180 136 360 150 552 186V196C360 164 180 152 0 160Z" fill="#ffffff" opacity=".35"/>
    <path d="M0 246C180 236 360 252 552 288V298C360 266 180 254 0 260Z" fill="#ffffff" opacity=".35"/>
    <path d="M0 346C180 336 360 352 552 388V398C360 366 180 354 0 360Z" fill="#ffffff" opacity=".35"/>
    <path d="M0 420C120 402 260 402 360 412V436C260 426 120 428 0 452Z" fill="var(--shadow)"/>
    <path d="M0 680C150 650 330 600 552 560V598C360 628 170 672 0 706Z" fill="var(--sky)" opacity="0"/>
  </svg>

  <div class="photo photo--bed" style="top:58px" role="img" aria-label="Photo of a twin pillow-top mattress"></div>
  <div class="photo photo--bed" style="top:158px" role="img" aria-label="Photo of a full mattress"></div>
  <div class="photo photo--bed" style="top:262px" role="img" aria-label="Photo of a queen mattress"></div>
  <div class="photo photo--bed" style="top:358px" role="img" aria-label="Photo of a king mattress"></div>

  <div class="price-list">
    <div class="price" style="top:64px">$99</div>
    <p class="price-label" style="top:76px">TWIN BED</p>
    <div class="price" style="top:164px">$159</div>
    <p class="price-label" style="top:176px">FULL BED</p>
    <div class="price" style="top:264px">$199</div>
    <p class="price-label" style="top:276px">QUEEN BED</p>
    <div class="price" style="top:364px">$299</div>
    <p class="price-label" style="top:376px">KING BED</p>
  </div>

  <div class="photo photo--woman" role="img" aria-label="Photo of a cheerful woman in jeans pointing at the prices"></div>

  <div class="call"><span class="call__word">CALL</span><span class="call__phone">(786)555-0147</span></div>

  <div class="brand"><span class="brand__name">Bayside Mattress</span><span class="brand__sub">OUTLET</span></div>
  <p class="address">10420 SW, 172ST, MIAMI, FL 33157</p>

  <div class="partners">
    <span class="partners__item"><i class="partners__dot"></i>KELLBROOK</span>
    <span class="partners__item">Dormo</span>
    <span class="partners__item">Restova</span>
    <span class="partners__item">Vale &amp; Pruitt</span>
    <span class="partners__more">and other<br>great brand names!</span>
  </div>
</section>

</body>
</html>
```